Ridgemark Construction Letterhead

Looking for a new professional letter head for our business with one of the two logos on it. It must include all of the information listed below. The company is a heavy construction company and should have something strong looking to go along with the business. Needs to include all of the information we have listed, with nothing added. Looking for something that represents our business well. Would like it to be clean looking with nothing too fancy or colorful. Needs to be bold and strong.

Industry/Entity Type

Construction Company

Font styles to use
Sans Serif

Requirements
Must have
• One of the two logos attached
• Address - 718 Quarry Bend Rd, Niagara on the Lake, ON L0S 2K4
• Phone Number - 905-614-3871
• Fax Number - 905-614-3894
• Website - www.ridgemarkconstruction.ca
Nice to have
• Something clean and professional looking
Should not have
• Should not have the words "address", "phone number", etc.
• Only wrote those to have that info included

```html
<!DOCTYPE html>
<html lang="en">
<head>
<meta charset="utf-8">
<title>Ridgemark Construction Letterhead</title>
<link rel="stylesheet" href="https://fonts.googleapis.com/css2?family=Montserrat:wght@500;700;800;900&family=Open+Sans:wght@400&display=swap">
<style>
  :root {
    --ink: #0d0d0d;
    --gold: #9b7a3c;
    --paper: #ffffff;
    --stage-grey: #8e8d8e;
    --stage-teal: #a9dccf;
    --text: #1a1a1a;
  }
  * { margin: 0; padding: 0; box-sizing: border-box; }
  html, body { width: 1200px; height: 2914px; overflow: hidden; }
  body { position: relative; font-family: "Montserrat", sans-serif; }

  .stage { position: absolute; left: 0; width: 1200px; }
  .stage--grey { top: 0; height: 1488px; background: var(--stage-grey); }
  .stage--teal { top: 1488px; height: 1426px; background: var(--stage-teal); }

  .sheet {
    position: absolute;
    width: 340px;
    background: var(--paper);
    transform-origin: top left;
  }
  .sheet--blank { left: 192px; top: 161px; height: 481px; transform: scale(2.4); }
  .sheet--letter { left: 158px; top: 1603px; height: 488px; transform: scale(2.47); }

  .top-bar { position: absolute; left: 0; top: 0; width: 100%; height: 5px; background: var(--ink); }

  .brand-block {
    position: absolute; left: 50%; top: 7px;
    width: 71px; height: 74px; margin-left: -35.5px;
    background: var(--ink);
    display: flex; flex-direction: column; align-items: center;
  }
  .brand-block__square { width: 34px; height: 34px; margin-top: 4px; background: var(--gold); }
  .brand-block__name {
    margin-top: 5px; color: var(--paper);
    font-weight: 800; text-align: center; line-height: 1;
  }
  .brand-block__name span { display: block; }
  .brand-block__name .line-1 { font-size: 9.6px; letter-spacing: -0.2px; }
  .brand-block__name .line-2 { font-size: 6.2px; margin-top: 1.5px; letter-spacing: 0.1px; }

  .body-copy {
    position: absolute; left: 37px; top: 147px; width: 288px;
    font-family: "Open Sans", sans-serif; font-size: 3.05px; line-height: 4.45px;
    color: var(--text);
  }
  .body-copy p + p { margin-top: 4.45px; }

  .footer {
    position: absolute; left: 0; width: 100%;
    text-align: center; font-size: 3.2px; line-height: 4.3px; color: var(--text);
    font-weight: 500;
  }
  .sheet--blank .footer { top: 444px; }
  .sheet--letter .footer { top: 451px; }
  .footer__name { color: var(--gold); font-weight: 700; font-size: 3.5px; }
  .footer__label { color: var(--gold); font-weight: 700; }

  .bottom-bar { position: absolute; left: 0; bottom: 0; width: 100%; height: 3.5px; background: var(--ink); }
  .bottom-bar__accent { position: absolute; left: 113px; bottom: 0; width: 114px; height: 3.5px; background: var(--gold); }
</style>
</head>
<body>
  <div class="stage stage--grey"></div>
  <div class="stage stage--teal"></div>

  <section class="sheet sheet--blank">
    <div class="top-bar"></div>
    <div class="brand-block">
      <div class="brand-block__square"></div>
      <div class="brand-block__name"><span class="line-1">RIDGEMARK</span><span class="line-2">CONSTRUCTION</span></div>
    </div>
    <footer class="footer">
      <div class="footer__name">RIDGEMARK CONSTRUCTION</div>
      <div><span class="footer__label">A:</span> 718 Quarry Bend Rd, Niagara on the Lake, ON L0S 2K4</div>
      <div><span class="footer__label">Tel:</span> 905-614-3871 &nbsp;|&nbsp; <span class="footer__label">Fax:</span> 905-614-3894</div>
      <div>www.ridgemarkconstruction.ca</div>
    </footer>
    <div class="bottom-bar"></div>
    <div class="bottom-bar__accent"></div>
  </section>

  <section class="sheet sheet--letter">
    <div class="top-bar"></div>
    <div class="brand-block">
      <div class="brand-block__square"></div>
      <div class="brand-block__name"><span class="line-1">RIDGEMARK</span><span class="line-2">CONSTRUCTION</span></div>
    </div>
    <div class="body-copy">
      <p>Lorem ipsum dolor sit amet, consectetur adipisicing elit, sed do eiusmod tempor incididunt ut labore et dolore magna aliqua. Ut enim ad minim veniam, quis nostrud exercitation ullamco laboris nisi ut aliquip ex ea commodo consequat. Duis aute irure dolor in reprehenderit in voluptate velit esse cillum dolore eu fugiat nulla pariatur. Excepteur sint occaecat cupidatat non proident, sunt in culpa qui officia deserunt mollit anim id est laborum. Sed ut perspiciatis unde omnis iste natus error sit voluptatem accusantium doloremque laudantium, totam rem aperiam, eaque ipsa quae ab illo inventore veritatis et quasi architecto beatae vitae dicta sunt explicabo. Nemo enim ipsam voluptatem quia voluptas sit aspernatur aut odit aut fugit, sed quia consequuntur magni dolores eos qui ratione voluptatem sequi nesciunt. Neque porro quisquam est, qui dolorem ipsum quia dolor sit amet, consectetur, adipisci velit, sed quia non numquam eius modi tempora incidunt ut labore et dolore magnam aliquam quaerat voluptatem.</p>
      <p>Lorem ipsum dolor sit amet, consectetur adipisicing elit, sed do eiusmod tempor incididunt ut labore et dolore magna aliqua. Ut enim ad minim veniam, quis nostrud exercitation ullamco laboris nisi ut aliquip ex ea commodo consequat. Duis aute irure dolor in reprehenderit in voluptate velit esse cillum dolore eu fugiat nulla pariatur. Excepteur sint occaecat cupidatat non proident, sunt in culpa qui officia deserunt mollit anim id est laborum.</p>
      <p>sectetur, adipisci velit, sed quia non numquam eius modi tempora incidunt ut labore et dolore magnam aliquam quaerat voluptatem.</p>
    </div>
    <footer class="footer">
      <div class="footer__name">RIDGEMARK CONSTRUCTION</div>
      <div><span class="footer__label">A:</span> 718 Quarry Bend Rd, Niagara on the Lake, ON L0S 2K4</div>
      <div><span class="footer__label">Tel:</span> 905-614-3871 &nbsp;|&nbsp; <span class="footer__label">Fax:</span> 905-614-3894</div>
      <div>www.ridgemarkconstruction.ca</div>
    </footer>
    <div class="bottom-bar"></div>
    <div class="bottom-bar__accent"></div>
  </section>
</body>
</html>
```